TRENDY & MODERN BUSINESS CARD DESIGN for Media Company *

I need a minimalistic - clean - modern and professional business card layout and design for MEDIA & PHOTOGRAPHY STUDIO.

We do NOT have a logo, and not really looking for one - but rather excellent typography and design. We would consider the 3 as a focal point.

We do personal and commercial photography.

Target Market(s)

Personal and commercial photography clientele

Contact Information for Business Card

ZUB size - from zub.com / size guidelines are enclosed in the brief

Font styles to use
Sans Serif

Colors
f78f20
eda3c7
cee9f5
0555a3
e667a6
fbf289

Requirements
Must have
• Clean lines - Modern layout
Nice to have
• All blue background as an option - use color palette in brief please.
Should not have
• Old fashion fonts and regular fonts.

```html
<!DOCTYPE html>
<html lang="en">
<head>
<meta charset="utf-8">
<title>Northlight Studio — Business Card</title>
<link rel="stylesheet" href="https://fonts.googleapis.com/css2?family=Lato:wght@400&family=Rubik:wght@400;700&family=Oswald:wght@600&display=swap">
<style>
  :root {
    --page-bg: #d8d5d1;
    --purple-deep: #6a3d9e;
    --purple-mid: #5b4aa6;
    --blue-violet: #4a65b2;
    --ink-purple: #5a2d91;
    --paper: #ffffff;
    --shadow: rgba(40, 30, 60, 0.25);
  }
  * { box-sizing: border-box; margin: 0; padding: 0; }
  html, body { width: 1200px; height: 1200px; overflow: hidden; }
  body {
    background: var(--page-bg);
    display: flex;
    flex-direction: column;
    align-items: center;
    justify-content: center;
    gap: 44px;
    font-family: "Lato", sans-serif;
  }
  .card {
    width: 900px;
    height: 514px;
    position: relative;
    box-shadow: 0 10px 30px var(--shadow);
  }

  /* Front */
  .card-front {
    background: linear-gradient(35deg, var(--purple-deep) 0%, var(--purple-mid) 50%, var(--blue-violet) 100%);
    color: var(--paper);
    display: flex;
    flex-direction: column;
    align-items: center;
    justify-content: center;
  }
  .wordmark-front {
    font-family: "Lato", sans-serif;
    font-weight: 400;
    font-size: 56px;
    letter-spacing: 2px;
    line-height: 1;
    text-transform: uppercase;
  }
  .tagline-front {
    font-family: "Lato", sans-serif;
    font-size: 17px;
    letter-spacing: 4.5px;
    margin-top: 10px;
    text-transform: uppercase;
  }
  .cities {
    position: absolute;
    bottom: 44px;
    left: 0;
    right: 0;
    text-align: center;
    font-size: 14px;
    letter-spacing: 4px;
    text-transform: uppercase;
  }

  /* Back */
  .card-back {
    background: var(--paper);
    color: var(--ink-purple);
  }
  .brand-back {
    position: absolute;
    top: 70px;
    right: 70px;
    text-align: right;
  }
  .wordmark-back {
    font-family: "Rubik", sans-serif;
    font-weight: 700;
    font-size: 52px;
    line-height: 1;
    letter-spacing: 1px;
    text-transform: uppercase;
  }
  .tagline-back {
    font-family: "Rubik", sans-serif;
    font-weight: 400;
    font-size: 16px;
    letter-spacing: 4.2px;
    text-transform: uppercase;
    margin-top: 8px;
  }
  .contact-block {
    position: absolute;
    left: 70px;
    right: 60px;
    bottom: 62px;
  }
  .person {
    display: flex;
    align-items: baseline;
    gap: 16px;
  }
  .person-name {
    font-family: "Oswald", sans-serif;
    font-weight: 600;
    font-size: 46px;
    text-transform: uppercase;
    letter-spacing: 0.5px;
  }
  .person-title {
    font-family: "Rubik", sans-serif;
    font-size: 19px;
  }
  .contact-line {
    font-family: "Rubik", sans-serif;
    font-size: 16px;
    margin-top: 8px;
    display: flex;
    gap: 12px;
    white-space: nowrap;
  }
</style>
</head>
<body>
  <section class="card card-front">
    <h1 class="wordmark-front">Northlight Studio</h1>
    <p class="tagline-front">Frame Every Moment</p>
    <p class="cities">Miami · New York · Las Vegas · Cancun · Roma</p>
  </section>

  <section class="card card-back">
    <div class="brand-back">
      <h2 class="wordmark-back">Northlight Studio</h2>
      <p class="tagline-back">Frame Every Moment</p>
    </div>
    <div class="contact-block">
      <div class="person">
        <span class="person-name">Marina Ortega</span>
        <span class="person-title">Founder &amp; Media Director</span>
      </div>
      <p class="contact-line">
        <span>+(305) 555-0148</span><span class="sep">/</span>
        <span>marina@northlight.studio</span><span class="sep">/</span>
        <span>250 Harbor Lane, 4th Floor, Miami, FL 33130</span>
      </p>
    </div>
  </section>
</body>
</html>
```